Harbor Crest Metrics Company Website Design and Coding

We want to redesign our existing website so that it is more visually and functionally appealing to prospective clients and potential job candidates. We would like to keep our current color scheme and implement our current logo as well. We have a high-level idea of website structure that we are thinking of, which is in the attached files. Logo is included as well. The final design would ideally be energy and analytics focused. We will need the new website to be coded as well, please.
Updates

Target Market(s)

Energy and utility industry

Industry/Entity Type

Energy/analytics

Coding

Coded - Design and coding required

Number of Pages Required

5+ page

Font styles to use
Sans Serif

Colors
0094D4
00A9DD
6FCCEA
C7EBF8
E9F6FB
F0912C
F2A743
F7CA91
FBE8D2
FDF5EE

Requirements
Must have
• Consistent color scheme- please use the one that we provided. We need an overview, a home page, and our core services. A separate job application page. Logo must be incorporated. We would like e "Meet our Team" page. Please include all of the content that is listed in our attachments.
Nice to have
• Movement
Should not have
• No music, no cartoons/animation, no pictures of a chalkboard

```html
<!DOCTYPE html>
<html lang="en">
<head>
<meta charset="utf-8">
<title>Harbor Crest Metrics</title>
<link rel="stylesheet" href="https://fonts.googleapis.com/css2?family=Rubik:wght@400;500&family=Barlow:wght@400;500;600;700&display=swap">
<style>
:root{
  --blue:#0094d4;
  --blue-2:#00a9dd;
  --blue-soft:#6fccea;
  --ink:#1d1e21;
  --text:#4a4c52;
  --muted:#8a8d94;
  --grey-bg:#eeeff1;
  --icon-bg:#e1e2e5;
  --footer:#25262a;
  --footer-text:#b4b6bb;
  --white:#ffffff;
}
*{box-sizing:border-box;margin:0;padding:0}
html,body{width:1200px;height:3513px;overflow:hidden}
body{font-family:"Barlow",sans-serif;color:var(--text);background:var(--white);position:relative}
.abs{position:absolute}
.section{position:absolute;left:0;width:1200px}
.heading{font-family:"Rubik",sans-serif;font-weight:400;color:var(--ink)}
.accent{color:var(--blue)}
.eyebrow{font-size:9px;letter-spacing:3px;font-weight:600;color:var(--blue);text-transform:uppercase;text-align:center}
.eyebrow.lined::before,.eyebrow.lined::after{content:"";display:inline-block;width:14px;height:1px;background:var(--blue-soft);vertical-align:middle;margin:0 8px}
.btn{position:absolute;display:flex;align-items:center;justify-content:center;gap:6px;border-radius:20px;font-size:9px;font-weight:700;letter-spacing:.5px;text-transform:uppercase;color:var(--white);background:var(--blue)}
.center{text-align:center}

/* header + hero */
.hero{top:0;height:589px;background:radial-gradient(ellipse at 75% 40%,#16406b 0%,#0b1d35 40%,#050a14 80%)}
.nav{position:absolute;top:30px;left:130px;width:940px;height:26px;display:flex;align-items:center}
.brand{display:flex;align-items:center;gap:8px}
.brand-dot{width:22px;height:22px;border-radius:50%;border:2px solid var(--blue-2)}
.brand-name{font-family:"Barlow",sans-serif;font-size:14px;font-weight:500;color:var(--blue-soft)}
.menu{margin-left:auto;display:flex;gap:17px;align-items:center;font-size:8.5px;font-weight:700;color:var(--white);text-transform:uppercase}
.menu .active{color:var(--blue-2)}
.menu .sep{width:1px;height:10px;background:#5b6577}
.nav .btn{position:static;height:22px;padding:0 14px;margin-left:14px}
.hero h1{position:absolute;top:226px;width:100%;text-align:center;font-family:"Rubik",sans-serif;font-weight:500;font-size:37px;line-height:44px;color:var(--white)}
.hero p{position:absolute;top:325px;width:100%;text-align:center;font-size:11.5px;line-height:16px;color:#e6ebf2}
.btn-ghost{background:transparent;border:1.5px solid var(--white);height:28px;width:107px;left:547px;top:377px}

/* about */
.about{top:589px;height:420px}
.about-photo{position:absolute;left:130px;top:65px;width:470px;height:294px;border-radius:14px;background:linear-gradient(180deg,#a9d2f0 0%,#d8ecf6 35%,#6f9b58 55%,#4c7d3a 68%,#4d5f8a 80%,#2f3d66 100%)}
.play{position:absolute;left:569px;top:180px;width:62px;height:62px;border-radius:50%;background:var(--blue);display:flex;align-items:center;justify-content:center}
.about-copy{position:absolute;left:657px;top:70px;width:375px}
.about-copy .eyebrow{text-align:left}
.about-copy .eyebrow::after{content:"";display:inline-block;width:14px;height:1px;background:var(--blue-soft);vertical-align:middle;margin-left:8px}
.about-copy h2{font-size:30px;margin:8px 0 10px}
.about-copy p{font-size:10.5px;line-height:15.5px;margin-bottom:8px}
.about-copy .btn{position:static;width:112px;height:28px;margin-top:10px}
.rule{position:absolute;left:0;top:420px;width:1200px;height:1px;background:#eef0f3}
.rule-label{position:absolute;top:413px;left:0;width:1200px}
.rule-label span{background:var(--white);padding:0 12px}

/* excel strip */
.excel{top:1009px;height:296px}
.excel-item{position:absolute;top:65px;width:170px;margin-left:-85px;text-align:center}
.excel-badge{position:relative;width:68px;height:68px;margin:0 auto;border-radius:50%;background:var(--ink);display:flex;align-items:center;justify-content:center}
.excel-num{position:absolute;bottom:-9px;left:24px;width:20px;height:20px;border-radius:50%;background:var(--blue);color:var(--white);font-size:8px;font-weight:700;display:flex;align-items:center;justify-content:center;border:2px solid var(--white)}
.excel-badge.current{background:var(--white);border:3px solid var(--blue);box-shadow:inset 0 0 0 4px var(--white),inset 0 0 0 60px var(--ink);color:var(--white);font-family:"Rubik",sans-serif;font-size:20px}
.excel-item h3{font-size:10px;font-weight:600;color:var(--ink);text-transform:uppercase;margin-top:20px}
.excel-item.current h3{color:var(--blue);margin-top:10px}
.excel-item p{font-size:10px;line-height:14px;margin-top:6px}

/* services */
.services{top:1305px;height:574px;background:linear-gradient(180deg,var(--grey-bg),#f7f8f9)}
.services h2{position:absolute;top:88px;width:100%;text-align:center;font-size:30px}
.intro{position:absolute;width:100%;text-align:center;font-size:10.5px;line-height:15.5px}
.svc{position:absolute;width:230px}
.svc h4{font-size:9.5px;font-weight:700;color:var(--ink);text-transform:uppercase;margin-bottom:5px}
.svc p{font-size:10.5px;line-height:15.5px}
.svc.left{left:130px;text-align:right}
.svc.right{left:839px}
.svc.active h4{color:var(--blue)}
.svc-icon{position:absolute;width:57px;height:57px;border-radius:50%;background:var(--icon-bg);display:flex;align-items:center;justify-content:center}
.svc-icon.active{background:var(--blue)}
.hub{position:absolute;left:467px;top:192px;width:266px;height:266px;border-radius:50%;background:var(--white);box-shadow:0 4px 20px rgba(0,0,0,.1)}
.hub-fill{position:absolute;inset:6px;border-radius:50%;background:radial-gradient(circle at 50% 35%,#5a5c62,#2b2c30 70%);display:flex;flex-direction:column;align-items:center;justify-content:center}
.hub-name{font-size:16px;font-weight:500;color:var(--blue-soft);margin-top:40px}

/* testimonials */
.testimonials{top:1879px;height:412px;background:linear-gradient(120deg,#6b7280 0%,#4b515b 45%,#8a9097 100%)}
.testimonials::after{content:"";position:absolute;inset:0;background:rgba(20,24,30,.45)}
.testi-inner{position:absolute;inset:0;z-index:1;color:var(--white)}
.testimonials h2{position:absolute;top:86px;width:100%;text-align:center;font-size:30px;color:var(--white)}
.avatar{position:absolute;left:573px;top:156px;width:54px;height:54px;border-radius:50%;background:linear-gradient(#c6a58a,#7d5a47);border:3px solid var(--white)}
.quote{position:absolute;left:260px;top:225px;width:680px;text-align:center;font-size:13px;line-height:19px}
.stars{position:absolute;top:292px;width:100%;text-align:center;color:var(--blue);font-size:12px;letter-spacing:3px}
.person{position:absolute;top:318px;width:100%;text-align:center;font-size:11px;line-height:15px}
.person b{font-weight:700}
.arrow{position:absolute;top:243px}

/* work */
.work{top:2291px;height:573px}
.work h2{position:absolute;top:96px;width:100%;text-align:center;font-size:30px}
.card{position:absolute;top:191px;width:301px;height:300px;border-radius:12px}
.card-label{position:absolute;bottom:38px;width:100%;text-align:center;font-size:10px;font-weight:700;color:var(--white);text-transform:uppercase}
.card-icon{position:absolute;bottom:-18px;left:50%;margin-left:-20px;width:40px;height:40px;border-radius:50%;background:var(--white);box-shadow:0 2px 8px rgba(0,0,0,.1);display:flex;align-items:center;justify-content:center}
.card-feature{background:linear-gradient(#4a4b50,#2d2e32);color:var(--white);text-align:center}
.card-feature h3{margin-top:30px;font-family:"Rubik",sans-serif;font-weight:500;font-size:15px;line-height:20px}
.card-feature p{margin:10px 30px 0;font-size:10px;line-height:15px}
.card-feature .btn{left:89px;top:138px;width:123px;height:27px}

/* contact band */
.contact{top:2864px;height:267px;background:linear-gradient(180deg,#dfe5ec 0%,#b9c6d4 60%,#8a9bb0 100%)}
.contact h2{position:absolute;top:92px;width:100%;text-align:center;font-size:30px}
.contact p{position:absolute;top:130px;width:100%;text-align:center;font-size:11px;color:var(--ink)}
.contact .btn{left:552px;top:172px;width:96px;height:28px}

/* footer */
.footer{top:3131px;height:382px;background:var(--footer);border-top:2px solid var(--blue);color:var(--footer-text)}
.foot-brand{position:absolute;left:130px;top:68px;width:110px;text-align:center}
.foot-brand .brand-dot{margin:0 auto 10px}
.foot-brand .brand-name{font-size:13px}
.follow{font-size:9.5px;margin-top:14px}
.socials{display:flex;gap:8px;justify-content:center;margin-top:8px}
.socials span{width:22px;height:22px;border-radius:50%;border:1px solid #6b6d73}
.col{position:absolute;top:70px;font-size:9.5px;line-height:13.5px}
.col h5{font-size:8px;font-weight:600;letter-spacing:.3px;color:var(--footer-text);text-transform:uppercase}
.col h5::after{content:"";display:block;width:16px;height:1.5px;background:var(--blue);margin:8px 0 10px}
.col li{list-style:none;color:var(--white);margin-bottom:6.5px}
.col .lbl{color:var(--footer-text)}
.newsletter-field{margin-top:10px;width:202px;height:26px;border-radius:14px;border:1px solid #55575d;display:flex;align-items:center;justify-content:space-between;padding:0 14px;color:#74767c;font-size:9px}
.legal{position:absolute;left:130px;top:3482px;width:940px;display:flex;font-size:8.5px;color:var(--footer-text)}
.legal .links{margin-left:auto;display:flex;gap:10px;color:var(--white);font-weight:600;text-transform:uppercase}
</style>
</head>
<body>

<header class="section hero" role="img" aria-label="Dark blue digital energy and data visualisation backdrop">
  <nav class="nav">
    <div class="brand"><span class="brand-dot"></span><span class="brand-name">Harbor Crest Metrics</span></div>
    <div class="menu">
      <span class="active">Home</span><span>Core Services ⌄</span><span>About ⌄</span><span>Our Work ⌄</span><span>Blog</span><span>Contact Us</span>
      <span class="sep"></span>
      <span>
        <svg width="9" height="9" viewBox="0 0 24 24" fill="none" stroke="#fff" stroke-width="2.5"><path d="M5 3h4l2 5-3 2a12 12 0 0 0 6 6l2-3 5 2v4a2 2 0 0 1-2 2A17 17 0 0 1 3 5a2 2 0 0 1 2-2z"/></svg>
        555.010.4827</span>
    </div>
    <span class="btn">▣ Get Started</span>
  </nav>
  <h1>Building A Smarter &amp;<br>Cleaner Energy Future</h1>
  <p>Harbor Crest Metrics is a consulting company that helps utilities and regulatory agencies<br>navigate the challenges of building a smarter and cleaner energy future.</p>
  <span class="btn btn-ghost">Explore More</span>
</header>

<section class="section about">
  <div class="about-photo" role="img" aria-label="Wind turbines and solar panels on green hills under a cloudy sky"></div>
  <div class="play"><svg width="14" height="14" viewBox="0 0 24 24" fill="none" stroke="#fff" stroke-width="2"><path d="M7 4l13 8-13 8z"/></svg></div>
  <div class="about-copy">
    <div class="eyebrow">About</div>
    <h2 class="heading">Company Overview</h2>
    <p>Harbor Crest Metrics (HCM) was formed in 2016 to help utilities and regulatory agencies navigate the technical, economic, and policy challenges of building a smarter and cleaner energy future. Our research focuses on impact analysis as well as predictive and causal analytics.</p>
    <p>We deliver data-driven insights into how various technologies and interventions affect the way homes and businesses use energy and how those in turn affect grid and system planning. We have a proven record for conducting high-quality, accurate, and unbiased analysis and are meticulous about ensuring that research is useful for policy decisions, operations, and implementation.</p>
    <span class="btn">More About Us</span>
  </div>
  <div class="rule"></div>
  <div class="rule-label eyebrow"><span>We Excel At</span></div>
</section>

<section class="section excel">
  <div class="excel-item" style="left:239px">
    <div class="excel-badge"><svg width="26" height="26" viewBox="0 0 24 24" fill="none" stroke="#fff" stroke-width="1.4"><path d="M4 5h16l-6 8v6l-4 2v-8z"/><circle cx="12" cy="3" r="1"/></svg><span class="excel-num">01</span></div>
    <h3>Research</h3><p>Data driven research and insights</p>
  </div>
  <div class="excel-item" style="left:419px">
    <div class="excel-badge"><svg width="26" height="26" viewBox="0 0 24 24" fill="none" stroke="#fff" stroke-width="1.4"><path d="M3 11l9-7 9 7"/><path d="M5 10v10h14V10"/><circle cx="12" cy="14" r="2.5"/></svg><span class="excel-num">02</span></div>
    <h3>Technologies</h3><p>Assessing how technologies and interventions affect energy use</p>
  </div>
  <div class="excel-item current" style="left:600px">
    <div class="excel-badge current">03</div>
    <h3>Planning</h3><p>Analyzing how changes in load affects system and T&amp;D planning</p>
  </div>
  <div class="excel-item" style="left:780px">
    <div class="excel-badge"><svg width="26" height="26" viewBox="0 0 24 24" fill="none" stroke="#fff" stroke-width="1.4"><rect x="4" y="4" width="16" height="16" rx="1"/><path d="M7 16l4-4 3 3 4-5"/></svg><span class="excel-num">04</span></div>
    <h3>Analytics</h3><p>Causal inference and predictive analytics</p>
  </div>
  <div class="excel-item" style="left:960px">
    <div class="excel-badge"><svg width="26" height="26" viewBox="0 0 24 24" fill="none" stroke="#fff" stroke-width="1.4"><rect x="6" y="3" width="13" height="17" rx="1"/><path d="M9 8h7M9 12h7M9 16h4"/><circle cx="6" cy="15" r="3"/></svg><span class="excel-num">05</span></div>
    <h3>Tools</h3><p>Building scalable tools that can be integrated into operations and planning</p>
  </div>
</section>

<section class="section services">
  <div class="eyebrow lined abs" style="top:67px;width:100%">Our Services</div>
  <h2 class="heading">What <span class="accent">We Do</span></h2>
  <p class="intro" style="top:128px">Lorem Ipsum is simply dummy text of the printing and typesetting industry. Lorem Ipsum has been<br>the industry's standard dummy text</p>

  <div class="svc left" style="top:195px"><h4>Predictive Analytics and Forecasting</h4><p>Lorem Ipsum is simply dummy text of the printing and typesetting industry. Lorem Ipsum has</p></div>
  <div class="svc-icon" style="left:374px;top:193px"><svg width="18" height="18" viewBox="0 0 24 24" fill="none" stroke="#555" stroke-width="1.5"><path d="M3 3v18h18"/><path d="M7 17v-4M11 17v-7M15 17v-5M19 17V8"/></svg></div>
  <div class="svc left" style="top:290px"><h4>T&amp;D Planning</h4><p>Lorem Ipsum is simply dummy text of the printing and typesetting industry. Lorem Ipsum has</p></div>
  <div class="svc-icon" style="left:374px;top:288px"><svg width="18" height="18" viewBox="0 0 24 24" fill="none" stroke="#555" stroke-width="1.5"><path d="M9 18h6M10 21h4"/><path d="M12 3a6 6 0 0 0-3 11v2h6v-2a6 6 0 0 0-3-11z"/></svg></div>
  <div class="svc left" style="top:384px"><h4>Evaluation</h4><p>Lorem Ipsum is simply dummy text of the printing and typesetting industry. Lorem Ipsum has</p></div>
  <div class="svc-icon" style="left:374px;top:382px"><svg width="18" height="18" viewBox="0 0 24 24" fill="none" stroke="#555" stroke-width="1.5"><path d="M14 3H5v18h14V8z"/><circle cx="11" cy="13" r="3"/><path d="M13 15l3 3"/></svg></div>

  <div class="hub"><div class="hub-fill" role="img" aria-label="Dark laptop workspace behind the company name"><span class="hub-name">Harbor Crest Metrics</span></div></div>

  <div class="svc-icon" style="left:769px;top:193px"><svg width="18" height="18" viewBox="0 0 24 24" fill="none" stroke="#555" stroke-width="1.5"><circle cx="12" cy="12" r="8"/><path d="M8 12l3 3 5-6"/></svg></div>
  <div class="svc right" style="top:195px"><h4>Pilot &amp; Emerging Tech Support</h4><p>Lorem Ipsum is simply dummy text of the printing and typesetting industry. Lorem Ipsum has</p></div>
  <div class="svc-icon active" style="left:769px;top:288px"><svg width="18" height="18" viewBox="0 0 24 24" fill="none" stroke="#fff" stroke-width="1.8"><path d="M4 12h14M13 7l5 5-5 5"/></svg></div>
  <div class="svc right active" style="top:290px"><h4>Program Portfolio &amp; Resource Planning</h4><p>Lorem Ipsum is simply dummy text of the printing and typesetting industry. Lorem Ipsum has</p></div>
  <div class="svc-icon" style="left:769px;top:382px"><svg width="18" height="18" viewBox="0 0 24 24" fill="none" stroke="#555" stroke-width="1.5"><path d="M21 3L3 10l7 3 3 7z"/><path d="M10 13l11-10"/></svg></div>
  <div class="svc right" style="top:384px"><h4>Program Delivery Support</h4><p>Lorem Ipsum is simply dummy text of the printing and typesetting industry. Lorem Ipsum has</p></div>

  <span class="btn" style="left:538px;top:478px;width:124px;height:29px">View All Services</span>
</section>

<section class="section testimonials" role="img" aria-label="Hands typing on a laptop showing charts on a desk">
  <div class="testi-inner">
    <div class="eyebrow lined abs" style="top:68px;width:100%">Testimonials</div>
    <h2 class="heading">What Our <span class="accent">Clients Say</span></h2>
    <div class="avatar" role="img" aria-label="Client portrait"></div>
    <p class="quote">“Lorem Ipsum is simply dummy text of the printing and typesetting industry. Lorem Ipsum has been the industry's standard dummy text ever since the 1500s, when an unknown printer took a galley of type and scrambled it to make a type specimen book.”</p>
    <div class="stars">★★★★★</div>
    <div class="person"><b>Daniel</b><br>Whitcombe</div>
    <svg class="arrow" style="left:207px" width="12" height="20" viewBox="0 0 12 20" fill="none" stroke="#fff" stroke-width="1.2" opacity=".6"><path d="M10 2L2 10l8 8"/></svg>
    <svg class="arrow" style="left:981px" width="12" height="20" viewBox="0 0 12 20" fill="none" stroke="#fff" stroke-width="1.2" opacity=".6"><path d="M2 2l8 8-8 8"/></svg>
  </div>
</section>

<section class="section work">
  <div class="eyebrow lined abs" style="top:70px;width:100%">Our Work</div>
  <h2 class="heading">Lorem Ipsum Is <span class="accent">Dummy Text</span></h2>
  <p class="intro" style="top:134px">Lorem Ipsum is simply dummy text of the printing and typesetting industry. Lorem Ipsum has been<br>the industry's standard dummy text ever since the 1500s</p>

  <div class="card" style="left:130px;background:linear-gradient(135deg,#d4d6da,#8d8f94 60%,#5d5f64)" role="img" aria-label="Person writing notes with a pen">
    <span class="card-label">Case Studies</span>
    <span class="card-icon"><svg width="15" height="15" viewBox="0 0 24 24" fill="none" stroke="#0094d4" stroke-width="1.6"><path d="M14 3H5v18h14V8z"/><circle cx="11" cy="13" r="3"/><path d="M13 15l3 3"/></svg></span>
  </div>
  <div class="card card-feature" style="left:450px">
    <h3>Journal Articles and Conference<br>Presentations</h3>
    <p>Lorem Ipsum is simply dummy text of the printing and typesetting industry. Lorem Ipsum has been the industry's standard dummy text ever since the 1500s</p>
    <span class="btn">View All Articles</span>
    <svg class="abs" style="left:144px;top:255px" width="13" height="15" viewBox="0 0 24 24" fill="none" stroke="#0094d4" stroke-width="1.6"><path d="M14 3H5v18h14V8z"/><path d="M8 13h8M8 17h6"/></svg>
  </div>
  <div class="card" style="left:769px;background:linear-gradient(135deg,#e6e7ea,#a8abb0 55%,#7c7f85)" role="img" aria-label="Laptop showing report charts">
    <span class="card-label">Reports</span>
    <span class="card-icon"><svg width="15" height="15" viewBox="0 0 24 24" fill="none" stroke="#0094d4" stroke-width="1.6"><circle cx="12" cy="12" r="9"/><path d="M12 3v9h9"/></svg></span>
  </div>
</section>

<section class="section contact" role="img" aria-label="Hand touching a network of connected contact icons">
  <div class="eyebrow lined abs" style="top:70px;width:100%">Contact Us</div>
  <h2 class="heading">Get In Touch</h2>
  <p>Please fill out the form below and we'll get back to you shortly.</p>
  <span class="btn"><svg width="9" height="9" viewBox="0 0 24 24" fill="none" stroke="#fff" stroke-width="2.5"><path d="M21 3L3 10l7 3 3 7z"/></svg>Email Us</span>
</section>

<footer class="section footer">
  <div class="foot-brand">
    <span class="brand-dot" style="display:block;width:26px;height:26px"></span>
    <span class="brand-name">Harbor Crest Metrics</span>
    <div class="follow">Follow Us:</div>
    <div class="socials"><span></span><span></span><span></span></div>
  </div>
  <div class="col" style="left:308px"><h5>About</h5><ul><li>Home</li><li>Company Overview</li><li>Our Team</li><li>Careers</li><li>Blog</li><li>Contact Us</li></ul></div>
  <div class="col" style="left:443px;width:115px"><h5>Core Services</h5><ul><li>Predictive Analytics and Forecasting</li><li>T&amp;D Planning</li><li>Evaluation</li><li>Pilot &amp; Emerging Tech Support</li><li>Program Portfolio &amp; Resource Planning</li><li>Program Delivery Support</li></ul></div>
  <div class="col" style="left:578px;width:115px"><h5>Our Work</h5><ul><li>Case Studies</li><li>Journal Articles and Conference Presentations</li><li>Reports</li></ul></div>
  <div class="col" style="left:714px;width:140px"><h5>Contact</h5><ul>
    <li><span class="lbl">Address:</span><br>418 Beacon Hill Rd, Suite 12, Riverton, GA 30199</li>
    <li><span class="lbl">Phone:</span><br>555.010.4827</li>
    <li><span class="lbl">Email:</span><br>info@harborcrestmetrics.com</li></ul></div>
  <div class="col" style="left:868px;width:202px"><h5>Newsletter</h5>
    <p>Subscribe to our emailing list. orem Ipsum is simply dummy text of the printing and typesetting industry.</p>
    <div class="newsletter-field"><span>Your Email Address</span><svg width="11" height="9" viewBox="0 0 24 18" fill="none" stroke="#b4b6bb" stroke-width="2"><rect x="1" y="1" width="22" height="16"/><path d="M1 1l11 9 11-9"/></svg></div>
  </div>
</footer>
<div class="legal"><span>© Copyright 2022 Harbor Crest Metrics.</span><span class="links"><span>Privacy Policy</span><span style="color:#6b6d73">|</span><span>Terms &amp; Conditions</span></span></div>

</body>
</html>
```